Men's Health Coaching Business - UK based

I am a UK based Health Coach who requires a clean Word Press 'lifestyle' design. The website will be a window to my services and is not intended to be a place to hang volumes of information off. It needs to be professional looking but with a hint of fun; easy/fun to navigate, intuitive and pleasing to the eye.

The site needs to be image/icon/video based to attract potential clients to my health coaching service. it should also encompass a creative/strong 'Call to Action' throughout the site - i.e. 'contact me'. I will only be using plain circle and plain circle for social media. Please also consider the colours of the beach/ocean and other lifestyle images I intend to you.

Images in your submission:

I am doing a photoshoot in July/Aug and so there is no need seek 'ideal images' as I will have a personal catalogue to choose from - examples along the lines of the above brief will be fine in your submission.

Good luck, I look forward to your submissions. Thank you.

Target Market(s)

My target audience is successful/professional men aged 30+ who are likely to lead busy lives, Dads, and enjoy hobbies/activities that keep them fit and healthy. They are probably cash-rich but time-poor - hence the clean, intuitive requirement for the site. I am also male who has a family. I require the site to have a slightly more masculine look/feel to it i.e. font, shapes etc. It must also compliment my logo coaching philosophy (see below).

Industry/Entity Type

Health

Font styles to use
Sans Serif

Colors

Designer to choose colors to be used in the design.

Requirements
Must have
• I have uploaded my logo for reference and inspiration and some images that are similar to the those that will be used throughout the site. The concept is below, but please feel free to employ your 'creative genius' to how it will operate/look/work; In broad terms, I require the following:
• 1 (Home Page): This will need to strongly convey the 'Why' to clients using my services by 1. showcasing who I am (My Story) through a Vimeo/Youtube; 2. showing results of previous clients through an eye-catching testimonials section; and 3. conveying to clients (as creatively as possible) the comprehensive approach of my coaching business; through the following elements (if this can be represented through an eye-catching graphic that chimes with my logo - even better):
• - Nutrition
• - Exercise
• - Mental well-being
• - Sleep - adequate/quality
• - Play - rest and recuperation
• - Sunlight - adequate
• - Plan, execute, review
• 2. 'My Philosophy' page: This will contain a number of paragraphs outlining to potential clients my guiding principles. The headings for each paragraph are:
• - I empathise - I'm a busy family man.
• - I choose my clients extremely carefully.
• - I guide, you decide.
• - I give it to you straight.
• - I give you the tools to change, build great health and see results.
• - If you don't fully commit, we'll part company.
• - I'm evidence-based and results driven.
• - I trust the numbers.
• - Consistency over perfection.
• - I take a comprehensive approach.
• - Guiding principles, not a prescriptive programme.
• - I will recommend some products - I don't sell them.
• - I use technology when it's complimentary.
• - Exercise is important but it's not the only factor.
• - I keep it simple for success.
• - I incorporate interventions that give you the biggest bang for your buck.
• - My guidance is designed to blend with your life.
• - I take a layered and progressive approach.
• - We'll have fun with the process.
• On the philosophy page, the images will be more atuned to preparing meals with the kids in the kitchen and images depicting other aspects of the key pillars such as Play - games with the kids, hobbies, activities or sports; rest and recuperation (reading, holidays etc); and using your brain.
• 3. The 'Investment' page (my prices page). This page needs to show three different packages: Bronze, Silver and Gold. An editable info-graph for ease of readability and showing what the client gets for each package/cost.
• Page 4. The 'Project You' Page. This page will show the client journey; ideally, icon/graphic driven, it should show a typical journey for a client, incorporating the following (taken from the Bronze Package) - please make this quick and fun to view:
• - Meet-up: coffee shop, telephone/video call.
• - Client completes e-Questionnaire.
• - Client records a 'typical week' in a journal.
• - Analyse/discuss e-Questionnaire with the client.
• - Analyse/discuss journal with the client.
• - Testing - Health Markers.
• - Testing - Body Composition Measurement.
• - Fitness Testing (if required) - tailored to sport/activity and preference.
• - Intervention Design and Refine.
• - Clients keep a journal of progress + supporting Meet/Video/telephone consultations.
• - 3-month: re-testing of Health Markers, Body Composition and Fitness.
• The Silver and Gold packages incorporate further testing and interventions as required.
• Page 5. The 'Exercise Sessions' page - VLOG. This page will hold a catalogue of home-based exercise films via Vimeo/Youtube for clients to use/refer to/follow anytime/anywhere. For each post/session I require a template that (as creatively as possible) can:
• - Hold a video;
• - Incorporate an editable info-graph that allows me to the following information fixed information.
• - Session title (header)
• - Exercise names (a maximum of 4 for each clip)
• Against each exercise I need to be able to show some or all of the following information - preferably icon/minimum words driven:
• - Intensity (i.e. low, medium, high, maximum)
• - Coaching points (be able to list of 4-5 key coaching points).
• - Safety points (to be able to list 4-5 key safety points).
• - Session goal (i.e. Strength, CV fitness; movement competency etc).
• - Session - Total time
• - Target heart rate during work (i.e. 150-160bpm)
• - Equipment options (i.e. bodyweight, kettle bell, power-bag, weighted bar, Olympic bar etc)
• - Sets.
• - Reps per set (i.e. 15 reps).
• - Duration per set (i.e. 30s).
• - Block sets (i.e. 3 x 3 sets)
• - Rest between sets (i.e. 30s)
• - Rest between block sets (i.e. 2 min)
• - Tempo (i.e. 2s-1s-3s)
• - Interval ratio (i.e. 30s work/10s rest)
• - Recover heart rate target (i.e. 120bpm)
• Viewable on other devices with no change in format.
Nice to have
• Whilst I need it to be professional, a little humour (design, quotes) would be great...
Should not have
• The look I definitely don't want - Bootcamp; gym/personal trainer; corporate; consultancy; feminine; flowery; fashion; cartoon; cluttered and confusing.

```html
<!DOCTYPE html>
<html lang="en">
<head>
<meta charset="utf-8">
<title>Ben Carrow – Health Coach</title>
<link href="https://fonts.googleapis.com/css2?family=Montserrat:wght@400;500;600;700&family=Open+Sans:wght@400;600&display=swap" rel="stylesheet">
<style>
:root{
  --teal:#17a59b;
  --teal-dark:#128a82;
  --ink:#111;
  --body:#6b6b6b;
  --soft-bg:#f6f6f6;
  --quote-bg:#f1f1f1;
  --footer-bg:#231f20;
  --footer-text:#bdbdbd;
  --white:#fff;
  --ghost:#ececec;
}
*{box-sizing:border-box;margin:0;padding:0}
html,body{width:1200px;height:2469px;overflow:hidden}
body{position:relative;background:var(--white);font-family:'Open Sans',sans-serif;color:var(--body)}
.abs{position:absolute}
.heading{font-family:'Montserrat',sans-serif;color:var(--ink);font-weight:600}
.center-x{left:0;width:1200px;text-align:center}
.rule{position:absolute;height:3px;background:var(--teal)}

/* hero */
.hero{left:0;top:0;width:1200px;height:494px;background:linear-gradient(160deg,#5b554f 0%,#3e3832 45%,#6b6157 75%,#2f2a26 100%)}
.hero::after{content:"";position:absolute;inset:0;background:rgba(0,0,0,.25)}
.brand{left:200px;top:14px;width:134px;text-align:center;z-index:2;color:var(--white)}
.brand-mark{width:40px;height:40px;border:3px solid var(--teal);border-radius:50%;margin:0 auto 6px}
.brand-name{font-family:'Montserrat',sans-serif;font-weight:600;font-size:19px;letter-spacing:1px;white-space:nowrap}
.brand-tag{font-family:'Montserrat',sans-serif;font-weight:600;font-size:8px;letter-spacing:2px;margin-top:2px}
.topbar{left:732px;top:38px;z-index:2;display:flex;align-items:center;color:var(--white);font-family:'Montserrat',sans-serif;font-size:18px;letter-spacing:1px}
.topbar svg{margin-right:10px}
.social{display:flex;gap:8px;margin-left:26px}
.social span{width:24px;height:24px;border-radius:50%;border:2px solid var(--teal)}
.social span+span{border-color:var(--white)}
.nav{left:561px;top:76px;z-index:2;font-family:'Montserrat',sans-serif;font-size:12px;color:var(--white);letter-spacing:.5px}
.nav a{color:inherit;text-decoration:none;position:absolute;white-space:nowrap}
.nav a.active{color:var(--teal)}
.nav a.active::after{content:"";position:absolute;left:0;right:0;top:21px;height:2px;background:var(--teal)}
.hero-mark{left:570px;top:197px;width:60px;height:60px;border:3px solid var(--white);border-radius:50%;z-index:2}
.hero-title{top:268px;z-index:2;font-family:'Montserrat',sans-serif;font-weight:600;font-size:29px;color:var(--teal);letter-spacing:.5px}
.hero-text{top:306px;left:370px;width:460px;z-index:2;text-align:center;color:var(--white);font-size:12.5px;line-height:18px}
.btn-primary{left:537px;top:365px;width:126px;height:30px;z-index:2;background:var(--teal);color:var(--white);border-radius:15px;font-family:'Montserrat',sans-serif;font-size:10.5px;font-weight:500;letter-spacing:1px;text-align:center;line-height:30px}
.slider-arrow{width:27px;height:27px;border-radius:50%;border:2px solid var(--white);z-index:2;display:flex;align-items:center;justify-content:center}
.slider-arrow.teal{border-color:var(--teal)}
.slider-arrow.grey{border:1.5px solid #9a9a9a;width:22px;height:22px}

/* about */
.about-photo{left:209px;top:459px;width:380px;height:402px;background:linear-gradient(180deg,#55707a 0%,#6f8f93 40%,#8a6e5d 75%,#b08070 100%);display:flex;flex-direction:column;align-items:center;justify-content:center;color:var(--white);font-family:'Montserrat',sans-serif;font-weight:600;font-size:17px}
.about-photo svg{margin-bottom:10px}
.ghost{font-family:'Montserrat',sans-serif;font-weight:700;color:var(--ghost);letter-spacing:2px;white-space:nowrap}
.body-text{font-size:12px;line-height:18.5px;color:var(--body)}
.read-more{font-size:11.5px;color:var(--teal);display:flex;align-items:center;gap:6px}
.read-more i{width:9px;height:9px;border-radius:50%;border:2px solid var(--teal);display:inline-block}

/* approach */
.approach{left:0;top:917px;width:1200px;height:471px;background:var(--soft-bg)}
.card{width:181px;height:227px;top:1103px;text-align:center}
.card.active{background:var(--teal)}
.card-icon{margin:28px auto 0;width:44px;height:44px;border:2.5px solid var(--teal);border-radius:10px}
.card.active .card-icon{border-color:var(--white)}
.card-title{margin-top:16px;font-family:'Montserrat',sans-serif;font-weight:600;font-size:17px;color:var(--ink)}
.card-rule{width:42px;height:3px;background:var(--teal);margin:8px auto 10px}
.card.active .card-title,.card.active .card-text,.card.active .read-more{color:var(--white)}
.card.active .card-rule{background:var(--white)}
.card.active .read-more i{border-color:var(--white)}
.card-text{font-size:11.5px;line-height:18.5px;padding:0 10px}
.card .read-more{justify-content:center;margin-top:10px}

/* testimonials */
.client-photo{left:209px;top:1546px;width:417px;height:415px;background:linear-gradient(135deg,#a9c7c9 0%,#8fb3b8 50%,#4f7fb0 100%)}
.quote-box{left:574px;top:1602px;width:417px;height:416px;background:var(--quote-bg)}
.quote-mark{left:650px;top:1630px;font-family:Georgia,serif;font-size:80px;color:#ddd;line-height:1}
.quote-text{left:668px;top:1660px;width:264px;font-size:11.5px;line-height:18.3px}
.quote-name{left:668px;width:280px;text-align:right;top:1917px;font-size:11.5px;font-weight:600;color:var(--teal)}
.quote-role{left:668px;width:280px;text-align:right;top:1937px;font-size:11.5px;color:var(--body)}

/* footer */
.footer{left:0;top:2074px;width:1200px;height:395px;background:var(--footer-bg)}
.f-title{font-family:'Montserrat',sans-serif;font-weight:500;font-size:17px;color:var(--white)}
.f-text{font-size:11.5px;line-height:18.5px;color:var(--footer-text)}
.f-input{left:209px;top:2239px;width:244px;height:29px;border-radius:15px;background:#3a3637;color:#8d8d8d;font-size:10.5px;line-height:29px;padding-left:16px}
.f-btn{left:209px;top:2290px;width:155px;height:30px;border-radius:15px;border:1.5px solid var(--teal);color:var(--teal);font-family:'Montserrat',sans-serif;font-size:10.5px;letter-spacing:1px;text-align:center;line-height:27px}
.f-links{left:545px;top:2184px;list-style:none;font-size:11.5px;line-height:21px;color:var(--footer-text)}
.f-links li::before{content:"» ";color:var(--footer-text)}
.f-contact{left:792px;top:2180px;font-size:11.5px;line-height:18.5px;color:var(--footer-text)}
.f-contact .row{display:flex;gap:9px;margin-bottom:10px}
.f-contact svg{flex:none;margin-top:4px}
.f-social{left:792px;top:2286px;display:flex;gap:10px}
.f-social span{width:25px;height:25px;border-radius:50%;border:1.5px solid var(--teal)}
.f-social span+span{border-color:#bbb}
.f-divider{left:209px;top:2364px;width:784px;height:1px;background:#444}
.to-top{left:587px;top:2350px;width:28px;height:28px;border-radius:50%;background:var(--teal);display:flex;align-items:center;justify-content:center}
.copyright{top:2402px;font-size:11px;color:var(--footer-text)}
</style>
</head>
<body>

<!-- hero -->
<section class="abs hero" role="img" aria-label="Photo of a smiling family at the beach"></section>
<div class="abs brand">
  <div class="brand-mark"></div>
  <div class="brand-name">BEN CARROW</div>
  <div class="brand-tag">HEALTH COACH</div>
</div>
<div class="abs topbar">
  <svg width="26" height="26" viewBox="0 0 26 26"><circle cx="13" cy="13" r="11.5" fill="none" stroke="#fff" stroke-width="2"/><path d="M9 7.5l2.5 0 1 3-1.6 1.2a7 7 0 0 0 3.4 3.4l1.2-1.6 3 1v2.5a1.5 1.5 0 0 1-1.6 1.5A10 10 0 0 1 7.5 9.1 1.5 1.5 0 0 1 9 7.5z" fill="#fff"/></svg>
  020 7946 0321
  <div class="social"><span></span><span></span></div>
</div>
<nav class="abs nav">
  <a class="active" style="left:0">Home</a>
  <a style="left:66px">About Us</a>
  <a style="left:157px">Approach</a>
  <a style="left:247px">Testimonials</a>
  <a style="left:356px">Contact Us</a>
</nav>
<div class="abs hero-mark"></div>
<h1 class="abs center-x hero-title">LIVE HEALTHY LIFE WITH US</h1>
<p class="abs hero-text">Sed vitae consectetur est, et mattis felis. Fusce lacinia nibh vitae fermentum finibus. Donec malesuada efficitur fermentum</p>
<div class="abs btn-primary">CONTACT ME</div>
<div class="abs slider-arrow" style="left:137px;top:284px"><svg width="8" height="10" viewBox="0 0 8 10"><path d="M6 1L2 5l4 4" fill="none" stroke="#fff" stroke-width="1.8"/></svg></div>
<div class="abs slider-arrow teal" style="left:1034px;top:284px"><svg width="8" height="10" viewBox="0 0 8 10"><path d="M2 1l4 4-4 4" fill="none" stroke="#17a59b" stroke-width="1.8"/></svg></div>

<!-- about -->
<div class="abs ghost" style="left:595px;top:548px;font-size:58px">ABOUT ME</div>
<div class="abs about-photo" role="img" aria-label="Photo of the coach standing by the sea">
  <svg width="38" height="38" viewBox="0 0 38 38"><circle cx="19" cy="19" r="17" fill="none" stroke="#fff" stroke-width="2.5"/><path d="M15 12l11 7-11 7z" fill="none" stroke="#fff" stroke-width="2.2" stroke-linejoin="round"/></svg>
  Watch Video
</div>
<h2 class="abs heading" style="left:634px;top:586px;font-size:27px">WHO AM I</h2>
<p class="abs heading" style="left:634px;top:638px;font-size:15.5px;font-weight:500">Hello, I am Ben Carrow</p>
<div class="rule" style="left:619px;top:670px;width:54px"></div>
<p class="abs body-text" style="left:634px;top:690px;width:352px">Lorem ipsum dolor sit amet, consectetur adipiscing elit. Curabitur id lobortis est. Vestibulum mauris purus, egestas et bibendum ac, sodales nec turpis. Donec ac ligula tristique, commodo nunc sit amet, varius urna. Etiam sem arcu, congue eget imperdiet bibendum, iaculis eget lacus.</p>
<div class="abs read-more" style="left:634px;top:790px">Read More <i></i></div>

<!-- approach -->
<section class="abs approach"></section>
<div class="abs ghost center-x" style="top:960px;font-size:54px;color:#eeeeee">WORK STYLE</div>
<h2 class="abs heading center-x" style="top:1002px;font-size:27px">COMPREHENSIVE APPROACH</h2>
<p class="abs center-x" style="top:1037px;font-size:11.5px">The comprehensive approach of my coaching business; through the following elements...</p>
<div class="rule" style="left:573px;top:1064px;width:54px"></div>
<div class="abs slider-arrow grey" style="left:137px;top:1206px"><svg width="7" height="9" viewBox="0 0 7 9"><path d="M5 1L2 4.5 5 8" fill="none" stroke="#999" stroke-width="1.5"/></svg></div>
<div class="abs slider-arrow grey" style="left:1034px;top:1206px"><svg width="7" height="9" viewBox="0 0 7 9"><path d="M2 1l3 3.5L2 8" fill="none" stroke="#999" stroke-width="1.5"/></svg></div>

<div class="abs card" style="left:207px"><div class="card-icon"></div><div class="card-title">Nutrition</div><div class="card-rule"></div><p class="card-text">Lorem ipsum dolor sit amet, consectetur adipiscing elit. Curabitur id lobortis.....</p><div class="read-more">Read More <i></i></div></div>
<div class="abs card active" style="left:408px"><div class="card-icon"></div><div class="card-title">Exercise</div><div class="card-rule"></div><p class="card-text">Lorem ipsum dolor sit amet, consectetur adipiscing elit. Curabitur id lobortis.....</p><div class="read-more">Read More <i></i></div></div>
<div class="abs card" style="left:609px"><div class="card-icon" style="border-radius:50%"></div><div class="card-title">Mental Well-Being</div><div class="card-rule"></div><p class="card-text">Lorem ipsum dolor sit amet, consectetur adipiscing elit. Curabitur id lobortis.....</p><div class="read-more">Read More <i></i></div></div>
<div class="abs card" style="left:810px"><div class="card-icon" style="border-radius:50%"></div><div class="card-title">Sleep Quality</div><div class="card-rule"></div><p class="card-text">Lorem ipsum dolor sit amet, consectetur adipiscing elit. Curabitur id lobortis.....</p><div class="read-more">Read More <i></i></div></div>

<!-- testimonials -->
<div class="abs ghost center-x" style="top:1432px;font-size:56px;color:#f0f0f0">TESTMONIALS</div>
<h2 class="abs heading center-x" style="top:1478px;font-size:26px">CUSTOMER FEEDBACK</h2>
<div class="abs slider-arrow grey" style="left:137px;top:1770px"><svg width="7" height="9" viewBox="0 0 7 9"><path d="M5 1L2 4.5 5 8" fill="none" stroke="#999" stroke-width="1.5"/></svg></div>
<div class="abs slider-arrow grey" style="left:1034px;top:1770px"><svg width="7" height="9" viewBox="0 0 7 9"><path d="M2 1l3 3.5L2 8" fill="none" stroke="#999" stroke-width="1.5"/></svg></div>
<div class="abs quote-box"></div>
<div class="abs client-photo" role="img" aria-label="Portrait photo of a satisfied client"></div>
<div class="abs quote-mark">“</div>
<div class="abs quote-text">
  <p>It is a long established fact that a reader will be distracted by the readable content of a page when looking at its layout. The point of using Lorem Ipsum is that it has a ore-or-less normal distribution of letters, as opposed to using 'Content here, content here', making it look like readable English.</p>
  <p style="margin-top:18px">It is a long established fact that a reader will be distracted by the readable content of a page when looking at its layout. The point of using Lorem Ipsum is that it has a ore-or-less normal distribution of letters</p>
</div>
<div class="abs quote-name">Lorem ipsume</div>
<div class="abs quote-role">CEO &amp; General manager</div>

<!-- footer -->
<footer class="abs footer"></footer>
<h3 class="abs f-title" style="left:209px;top:2127px">Subscribe Newsletter</h3>
<div class="rule" style="left:209px;top:2157px;width:42px"></div>
<p class="abs f-text" style="left:209px;top:2183px;width:260px">Subscribe to our newsletter to get the latest scoop right to your inbox</p>
<div class="abs f-input">Your Email Address</div>
<div class="abs f-btn">SUBSCRIBE NOW</div>

<h3 class="abs f-title" style="left:545px;top:2127px">Quick Links</h3>
<div class="rule" style="left:545px;top:2157px;width:42px"></div>
<ul class="abs f-links">
  <li>Home</li><li>About Us</li><li>Approach</li><li>Testimonails</li><li>Sitemap</li><li>Contact Us</li>
</ul>

<h3 class="abs f-title" style="left:792px;top:2127px">Contact Info</h3>
<div class="rule" style="left:792px;top:2157px;width:42px"></div>
<div class="abs f-contact">
  <div class="row"><svg width="10" height="10" viewBox="0 0 10 10"><path d="M1.5 0.5h2l1 2.5-1.3 1a5 5 0 0 0 2.8 2.8l1-1.3 2.5 1v2a1 1 0 0 1-1 1A9 9 0 0 1 0.5 1.5a1 1 0 0 1 1-1z" fill="#17a59b"/></svg>020 7946 0321</div>
  <div class="row"><svg width="11" height="9" viewBox="0 0 11 9"><rect x="0" y="0" width="11" height="9" rx="1" fill="#17a59b"/><path d="M0.5 1l5 4 5-4" fill="none" stroke="#231f20" stroke-width="1"/></svg>hello@bencarrow.co</div>
  <div class="row"><svg width="9" height="12" viewBox="0 0 9 12"><path d="M4.5 0A4.5 4.5 0 0 0 0 4.5C0 8 4.5 12 4.5 12S9 8 9 4.5A4.5 4.5 0 0 0 4.5 0z" fill="#17a59b"/><circle cx="4.5" cy="4.5" r="1.6" fill="#231f20"/></svg><span>Ben Carrow, 14 Harbour Row<br>Falmouth, TR11 3AB</span></div>
</div>
<div class="abs f-social"><span></span><span></span></div>

<div class="abs f-divider"></div>
<div class="abs to-top"><svg width="10" height="7" viewBox="0 0 10 7"><path d="M1 6l4-4 4 4" fill="none" stroke="#fff" stroke-width="1.8"/></svg></div>
<p class="abs center-x copyright">© 2017 Ben Carrow. All Rights Reserved</p>

</body>
</html>
```